Business Card, Stationery
Tax & Accounting Services
Professional
Lirena Vostrup EA
Tax Professional / Enrolled Agent
417 W Callory Avenue
Suite B
Bronx NY 10458
lvfiscalhub@quorvane.com
lvfiscalhub.com
Services:
Individual Tax Preparation
Business Tax Preparation
Tax Planning
DTB & State Tax Problems
Accounting
Payroll
Sales Tax
New Business Formation
Ledgerwell Setup

```html
<!DOCTYPE html>
<html lang="en">
<head>
<meta charset="utf-8">
<title>Callory Tax Group — Stationery Set</title>
<link href="https://fonts.googleapis.com/css2?family=Cinzel:wght@600&family=Open+Sans:wght@400;600&display=swap" rel="stylesheet">
<style>
:root{
  --stage:#e9e7e3;
  --paper:#ffffff;
  --navy:#1d3567;
  --red:#c22a30;
  --sky:#2a9cc9;
  --rule:#c9ced8;
  --ink:#3c4250;
  --ghost:#f1e2d4;
}
*{box-sizing:border-box;margin:0;padding:0}
html,body{width:1200px;height:562px;overflow:hidden;background:var(--stage);font-family:"Open Sans",sans-serif;color:var(--ink)}
.canvas{position:relative;width:1200px;height:562px}
.piece{position:absolute;background:var(--paper);box-shadow:0 2px 6px rgba(0,0,0,.18)}
.label{position:absolute;font-size:7px;font-weight:600;color:#333;text-align:center;width:100%;top:-11px}
.brand{font-family:"Cinzel",serif;font-weight:600;color:var(--navy);white-space:nowrap;display:flex;align-items:center;gap:5px}
.brand .dot{display:inline-block;background:var(--red);flex:none}
.ghost-brand{position:absolute;font-family:"Cinzel",serif;font-weight:600;color:var(--ghost);white-space:nowrap;text-align:center;width:100%}
.footer-band{position:absolute;left:0;right:0;bottom:0;height:26px;background:var(--navy);border-top:2px solid var(--red);color:#dfe5f0;font-size:5px;text-align:center;padding-top:5px;line-height:1.5}

/* fax */
.fax{left:29px;top:29px;width:355px;height:511px}
.fax .brand{position:absolute;top:22px;left:0;right:0;justify-content:center;font-size:15px}
.fax .brand .dot{width:10px;height:10px}
.fax-title{position:absolute;right:14px;top:72px;font-size:8px;font-weight:600;color:var(--navy)}
.fax-grid{position:absolute;left:14px;right:14px;top:82px;border:1px solid var(--rule);display:grid;grid-template-columns:1fr 1fr}
.fax-grid div{height:15px;border-bottom:1px solid var(--rule);font-size:6px;padding:4px 5px;display:flex;gap:6px}
.fax-grid div:nth-child(odd){border-right:1px solid var(--rule)}
.fax-grid div span.line{flex:1;border-bottom:1px solid #e2e5ea}
.fax-grid div:nth-last-child(-n+2){border-bottom:none}
.fax-checks{position:absolute;left:14px;right:14px;top:165px;display:flex;justify-content:space-between;font-size:5.5px}
.fax-checks span::before{content:"";display:inline-block;width:6px;height:6px;border:1px solid var(--ink);margin-right:3px;vertical-align:-1px}

/* letterhead */
.letterhead{left:403px;top:29px;width:360px;height:511px}
.letterhead .brand{position:absolute;top:22px;left:0;right:0;justify-content:center;font-size:15px}
.letterhead .brand .dot{width:10px;height:10px}
.ghost-brand.big{top:320px;font-size:30px}

/* cards */
.card{top:29px;width:118px;height:90px}
.card-front{left:773px}
.card-back{left:912px}
.card-front .brand{position:absolute;top:10px;left:8px;font-size:7px}
.card-front .brand .dot{width:5px;height:5px}
.card-contact{position:absolute;right:7px;top:30px;font-size:3.6px;line-height:1.55;text-align:right}
.card-contact b{font-size:4.6px;color:var(--navy)}
.card-front .band{position:absolute;left:0;right:0;bottom:6px;height:7px;background:linear-gradient(90deg,var(--navy),var(--sky))}
.card-back .brand{position:absolute;top:12px;left:8px;font-size:6px}
.card-back .brand .dot{width:4px;height:4px}
.card-services{position:absolute;left:62px;top:10px;font-size:3.5px;line-height:1.6;border-left:1px solid var(--red);padding-left:4px}
.card-back .band{position:absolute;left:0;right:0;bottom:0;height:6px;background:var(--navy);border-top:1px solid var(--red)}

/* envelope front */
.env-front{left:773px;top:149px;width:285px;height:163px}
.env-front .brand{position:absolute;top:16px;left:14px;font-size:12px}
.env-front .brand .dot{width:8px;height:8px}
.env-front .tag{position:absolute;left:14px;top:36px;font-size:4.5px;letter-spacing:.5px}
.env-front .band{position:absolute;left:0;right:0;bottom:10px;height:18px;background:linear-gradient(90deg,var(--navy),var(--sky) 60%,var(--navy));border-top:2px solid var(--red)}

/* envelope back */
.env-back{left:773px;top:343px;width:285px;height:197px}
.env-back svg{position:absolute;left:0;top:0}
.env-back .brand{position:absolute;top:112px;left:0;right:0;justify-content:center;font-size:8px}
.env-back .brand .dot{width:5px;height:5px}
.env-back .tag{position:absolute;top:125px;left:0;right:0;text-align:center;font-size:3.5px}
</style>
</head>
<body>
<main class="canvas">

  <section class="piece fax">
    <p class="label">Fax Cover</p>
    <div class="brand"><span class="dot"></span>Callory Tax Group</div>
    <p class="fax-title">FAX</p>
    <div class="fax-grid">
      <div>To: <span class="line"></span></div><div>From: <span class="line"></span></div>
      <div>Fax: <span class="line"></span></div><div>Pages: <span class="line"></span></div>
      <div>Phone: <span class="line"></span></div><div>Date: <span class="line"></span></div>
      <div>Re: <span class="line"></span></div><div>CC: <span class="line"></span></div>
    </div>
    <div class="fax-checks">
      <span>Urgent</span><span>For Review</span><span>Please Comment</span><span>Please Reply</span><span>Please Recycle</span>
    </div>
    <p class="ghost-brand big">Callory Tax Group</p>
    <div class="footer-band">417 W Callory Avenue, Suite B, Bronx NY 10458<br>P (718) 555-0142 · F (718) 555-0143 · lvfiscalhub@quorvane.com · lvfiscalhub.com</div>
  </section>

  <section class="piece letterhead">
    <p class="label">Letterhead</p>
    <div class="brand"><span class="dot"></span>Callory Tax Group</div>
    <p class="ghost-brand big">Callory Tax Group</p>
    <div class="footer-band">417 W Callory Avenue, Suite B, Bronx NY 10458<br>P (718) 555-0142 · F (718) 555-0143 · lvfiscalhub@quorvane.com · lvfiscalhub.com</div>
  </section>

  <section class="piece card card-front">
    <p class="label">Business Card (Front)</p>
    <div class="brand"><span class="dot"></span>Callory Tax Group</div>
    <div class="card-contact">
      <b>Lirena Vostrup EA</b><br>Tax Professional / Enrolled Agent<br>417 W Callory Avenue, Suite B<br>Bronx NY 10458<br>lvfiscalhub@quorvane.com<br>lvfiscalhub.com
    </div>
    <div class="band"></div>
  </section>

  <section class="piece card card-back">
    <p class="label">Business Card (Back)</p>
    <div class="brand"><span class="dot"></span>Callory Tax</div>
    <div class="card-services">
      Individual Tax Preparation<br>Business Tax Preparation<br>Tax Planning<br>DTB &amp; State Tax Problems<br>Accounting<br>Payroll<br>Sales Tax<br>New Business Formation<br>Ledgerwell Setup
    </div>
    <div class="band"></div>
  </section>

  <section class="piece env-front">
    <p class="label">Envelope (Front)</p>
    <div class="brand"><span class="dot"></span>Callory Tax Group</div>
    <p class="tag">417 W CALLORY AVENUE, SUITE B, BRONX NY 10458</p>
    <div class="band"></div>
  </section>

  <section class="piece env-back">
    <p class="label">Envelope (Back)</p>
    <svg width="285" height="197" viewBox="0 0 285 197">
      <polyline points="0,0 142,96 285,0" fill="none" stroke="var(--navy)" stroke-width="5"/>
      <polyline points="0,6 142,102 285,6" fill="none" stroke="var(--sky)" stroke-width="2"/>
      <line x1="0" y1="197" x2="120" y2="110" stroke="var(--rule)" stroke-width="1"/>
      <line x1="285" y1="197" x2="165" y2="110" stroke="var(--rule)" stroke-width="1"/>
    </svg>
    <div class="brand"><span class="dot"></span>Callory Tax Group</div>
    <p class="tag">417 W Callory Avenue, Suite B, Bronx NY 10458</p>
  </section>

</main>
</body>
</html>
```